Mara Lindqvist Advisory Business Cards

Hi - using the information and logo provided I require a two sided business card designed with the following information. The business card is a 'mini card' 3.5" x 1.25".

Front of card should be the logo attached but inverted (so the background is the peach colour and the logo white).

Back should have these details. If we can't fit the Instragram and Facebook part can we just put the little logos.

Mara Lindqvist

Art and Design Consultant
Dealer - Curator - Events - Styling - Creative Sourcing

P: 0438 519 207
E: mara@maralindqvistadvisory.com
W: www.maralindqvistadvisory.com
I (instagram image please): maralindqvistadvisory F (Facebook image please): MaraLindqvistAdvisor

Target Market(s)

Galleries, artists, art buyers, interior design clients, event managers, creative types

Industry/Entity Type

Business

```html
<!DOCTYPE html>
<html lang="en">
<head>
<meta charset="utf-8">
<title>Mara Lindqvist Advisory – Mini Business Card</title>
<link href="https://fonts.googleapis.com/css2?family=Questrial&display=swap" rel="stylesheet">
<style>
  :root {
    --backdrop: #d5d5d5;
    --paper: #ffffff;
    --peach: #f2bb9f;
    --peach-deep: #f0a884;
    --peach-faint: #fcebe2;
    --ink: #3b3b3b;
    --ink-soft: #5f5f63;
    --sans: "Questrial", "Century Gothic", sans-serif;
  }
  * { box-sizing: border-box; margin: 0; padding: 0; }
  html, body {
    width: 1200px; height: 900px; overflow: hidden;
    background: var(--backdrop);
    font-family: var(--sans);
  }
  .canvas { position: relative; width: 1200px; height: 900px; }

  /* Back of card: contact details */
  .card-back {
    position: absolute; left: 45px; top: 27px; width: 1127px; height: 402px;
    background: var(--paper);
  }
  .card-back__frame {
    position: absolute; left: 9px; top: 8px; right: 9px; bottom: 10px;
    border: 7px solid var(--peach);
  }
  .card-back__emblem {
    position: absolute; left: 771px; top: 66px; width: 270px; height: 270px;
    border-radius: 50%; background: var(--peach-faint);
    display: flex; align-items: center; justify-content: center; text-align: center;
    color: var(--paper); font-size: 26px; line-height: 1.25; letter-spacing: 2px;
  }
  .identity { position: absolute; left: 36px; top: 28px; }
  .identity__name { color: var(--peach-deep); font-size: 38px; line-height: 1; letter-spacing: 0.5px; }
  .identity__role { color: var(--ink); font-size: 25px; margin-top: 10px; }
  .identity__services { color: var(--peach-deep); font-size: 22px; margin-top: 4px; letter-spacing: 0.2px; }

  .contact-list { position: absolute; left: 28px; top: 178px; list-style: none; }
  .contact-list li {
    display: flex; align-items: center; height: 35px;
    color: var(--ink); font-size: 27px; letter-spacing: 0.3px;
  }
  .contact-list svg { width: 32px; height: 28px; margin-right: 10px; flex: none; }

  .social-list { position: absolute; left: 28px; top: 310px; list-style: none; }
  .social-list li {
    display: flex; align-items: center; height: 32px;
    color: var(--ink); font-size: 24px;
  }
  .social-list__mark {
    width: 22px; height: 22px; margin: 0 16px 0 4px;
    background: var(--peach); border-radius: 3px; flex: none;
  }

  /* Front of card: brand */
  .card-front {
    position: absolute; left: 45px; top: 452px; width: 1127px; height: 402px;
    background: var(--peach);
  }
  .card-front__frame {
    position: absolute; left: 11px; top: 12px; right: 12px; bottom: 13px;
    border: 5px solid var(--paper);
  }
  .card-front__disc {
    position: absolute; left: 75px; top: 51px; width: 300px; height: 300px;
    border-radius: 50%; background: var(--paper);
  }
  .wordmark {
    position: absolute; left: 423px; top: 130px; width: 685px;
    color: var(--ink-soft); text-transform: uppercase; text-align: center;
  }
  .wordmark__primary { font-size: 56px; letter-spacing: 9px; line-height: 1.1; }
  .wordmark__secondary { font-size: 34px; letter-spacing: 16px; margin-top: 22px; }
</style>
</head>
<body>
<main class="canvas">

  <section class="card-back" aria-label="Back of card">
    <div class="card-back__frame"></div>
    <div class="card-back__emblem">Mara Lindqvist<br>Advisory</div>

    <header class="identity">
      <h1 class="identity__name">Mara Lindqvist</h1>
      <p class="identity__role">Art and Design Consultant</p>
      <p class="identity__services">Dealer - Curator - Events - Styling - Creative Sourcing</p>
    </header>

    <ul class="contact-list">
      <li>
        <svg viewBox="0 0 32 28" aria-hidden="true">
          <path d="M7 3 L12 3 L14 9 L11 11 Q14 17 20 19 L22 16 L28 18 L28 23 Q27 26 23 26 Q8 24 4 8 Q4 4 7 3 Z" fill="var(--peach)"/>
        </svg>
        0438 519 207
      </li>
      <li>
        <svg viewBox="0 0 32 28" aria-hidden="true" fill="none" stroke="var(--peach)" stroke-width="2">
          <circle cx="15" cy="14" r="12"/>
          <ellipse cx="15" cy="14" rx="5.5" ry="12"/>
          <line x1="3" y1="14" x2="27" y2="14"/>
          <path d="M5 8 H25 M5 20 H25"/>
        </svg>
        www.maralindqvistadvisory.com
      </li>
      <li>
        <svg viewBox="0 0 32 28" aria-hidden="true">
          <rect x="2" y="6" width="27" height="17" fill="var(--peach)"/>
          <path d="M2 6 L15.5 16 L29 6" fill="none" stroke="var(--paper)" stroke-width="2"/>
        </svg>
        mara@maralindqvistadvisory.com
      </li>
    </ul>

    <ul class="social-list">
      <li><span class="social-list__mark"></span>maralindqvistadvisory</li>
      <li><span class="social-list__mark"></span>MaraLindqvistAdvisor</li>
    </ul>
  </section>

  <section class="card-front" aria-label="Front of card">
    <div class="card-front__frame"></div>
    <div class="card-front__disc"></div>
    <div class="wordmark">
      <p class="wordmark__primary">Mara Lindqvist</p>
      <p class="wordmark__secondary">Advisory</p>
    </div>
  </section>

</main>
</body>
</html>
```